A Maple Syrup Label for a Local Buniness

We are looking for a label for our maple syrup business. Our business currently sells honey, and we are expanding into maple syrup. Our Business name is "Brackley Honey" and we currently have a logo attached below. We would like to incorporate the bee and BH part, but the label could also read "Brackley Farms" with the words maple syrup. We do not want consumers to confuse the maple syrup jars with the honey jars. It should be clear that the jars contain maple syrup. We are open to new designs as well.

```html
<!DOCTYPE html>
<html lang="en">
<head>
<meta charset="utf-8">
<title>Brackley Honey – Maple Syrup Label</title>
<link rel="stylesheet" href="https://fonts.googleapis.com/css2?family=Libre+Baskerville:wght@700&family=Allura&display=swap">
<style>
  :root {
    --page: #e4e4e4;
    --plaid-light: #f1f1f1;
    --plaid-mid: #dcdcdc;
    --plaid-dark: #c9c9c9;
    --frame-black: #111111;
    --frame-gold: #c9a117;
    --panel-white: #f4f4f4;
    --ink: #141414;
  }
  * { margin: 0; padding: 0; box-sizing: border-box; }
  html, body {
    width: 1200px;
    height: 848px;
    overflow: hidden;
    background: var(--page);
  }
  .canvas {
    position: relative;
    width: 1200px;
    height: 848px;
  }
  .label {
    position: absolute;
    left: 120px;
    top: 63px;
    width: 960px;
    height: 722px;
    overflow: hidden;
  }
  .label__plaid {
    position: absolute;
    inset: 0;
    background: linear-gradient(100deg, var(--plaid-light) 0%, var(--plaid-mid) 45%, var(--plaid-light) 60%, var(--plaid-dark) 100%);
  }
  .badge {
    position: absolute;
    left: 224px;
    top: 53px;
    width: 513px;
    height: 615px;
  }
  .badge__frame {
    position: absolute;
    inset: 0;
    width: 100%;
    height: 100%;
  }
  .badge__content {
    position: absolute;
    inset: 0;
    display: flex;
    flex-direction: column;
    align-items: center;
    padding-top: 92px;
  }
  .brand-mark {
    width: 74px;
    height: 74px;
    border-radius: 50%;
    background: var(--frame-gold);
    margin-bottom: 22px;
  }
  .brand-name {
    font-family: "Libre Baskerville", serif;
    font-weight: 700;
    color: var(--ink);
    font-size: 46px;
    line-height: 1.08;
    text-align: center;
    letter-spacing: 0.5px;
  }
  .product-name {
    font-family: "Allura", cursive;
    color: var(--ink);
    font-size: 64px;
    line-height: 1;
    margin-top: 26px;
  }
  .leaf-icon {
    width: 80px;
    height: 80px;
    background: var(--ink);
    margin-top: 44px;
    border-radius: 6px;
  }
</style>
</head>
<body>
  <main class="canvas">
    <section class="label">
      <div class="label__plaid" role="img" aria-label="Grey buffalo-check plaid pattern with fine horizontal stripes"></div>

      <div class="badge">
        <svg class="badge__frame" viewBox="0 0 400 480" preserveAspectRatio="none" aria-hidden="true">
          <polygon fill="var(--frame-gold)" points="60,0 340,0 400,135 400,345 340,480 60,480 0,345 0,135"/>
          <polygon fill="var(--frame-black)" transform="translate(200 240) scale(0.985 0.988) translate(-200 -240)" points="60,0 340,0 400,135 400,345 340,480 60,480 0,345 0,135"/>
          <polygon fill="var(--frame-gold)" transform="translate(200 240) scale(0.93 0.942) translate(-200 -240)" points="60,0 340,0 400,135 400,345 340,480 60,480 0,345 0,135"/>
          <polygon fill="var(--panel-white)" transform="translate(200 240) scale(0.92 0.934) translate(-200 -240)" points="60,0 340,0 400,135 400,345 340,480 60,480 0,345 0,135"/>
        </svg>

        <div class="badge__content">
          <span class="brand-mark" aria-hidden="true"></span>
          <h1 class="brand-name">BRACKLEY<br>HONEY</h1>
          <p class="product-name">Maple Syrup</p>
          <div class="leaf-icon" role="img" aria-label="Black maple leaf emblem"></div>
        </div>
      </div>
    </section>
  </main>
</body>
</html>
```